4 page brochure for Logistics Company

Need a 4 page brochure (ie folded A3) for a Logistics company.
Service is a virtual network of warehouse and logistics companies.
Style is professional but accessible.
We have logo and styles designed and will upload these.
We have identified example images that could be used in the brochure.
Content will be uploaded also.
Updates
Reason: A couple of designers requested more time
Am giving another 24 hours to finalise and will then select most suitable design
Target Market(s)
40 to 60 year old business owners (traditional) - Australian
Industry/Entity Type
It Company
Requirements
Must have
- Professional
Should not have
- Nothing tacky

```html
<!DOCTYPE html>
<html lang="en">
<head>
<meta charset="utf-8">
<title>Meridian Logistics Group – Brochure Spread</title>
<link href="https://fonts.googleapis.com/css2?family=Source+Sans+3:wght@400;600;700&family=Ubuntu:wght@400;700&display=swap" rel="stylesheet">
<style>
  :root{
    --stage:#b4b4b4;
    --paper:#ffffff;
    --navy:#1f4e97;
    --deep:#173f86;
    --sky:#1aa3dc;
    --pale:#c9d6ec;
    --mist:#dfe6f3;
    --ink:#3a3a3a;
    --grey:#6b7680;
    --steel:#7f8c97;
  }
  *{box-sizing:border-box;margin:0;padding:0}
  html,body{width:1200px;height:939px;overflow:hidden;background:var(--stage)}
  body{font-family:"Source Sans 3",Arial,sans-serif;color:var(--ink)}
  .spread{position:absolute;left:0;top:45px;width:1200px;height:849px;overflow:hidden;background:var(--paper)}
  .spread-bg{position:absolute;inset:0}
  .page{position:absolute;top:0;height:849px;width:600px}
  .page-left{left:0}
  .page-right{left:600px}

  .brand{position:absolute;display:flex;align-items:center;gap:10px;color:var(--navy);font-weight:700;text-transform:uppercase;letter-spacing:.5px;line-height:1}
  .brand-mark{background:var(--navy);display:block}
  .brand-small{left:36px;top:74px;font-size:16px}
  .brand-small .brand-mark{width:22px;height:22px}
  .brand-large{left:150px;top:58px;font-size:26px}
  .brand-large .brand-mark{width:34px;height:34px}

  .route-map{position:absolute;left:400px;top:12px;width:165px;height:155px;border-radius:6px;background:radial-gradient(ellipse at 50% 45%,#eef0f4 0%,#e3e7ee 70%,rgba(255,255,255,0) 100%)}

  .section-title{position:absolute;left:38px;top:198px;font-size:17px;color:var(--navy);font-weight:400}
  .intro{position:absolute;left:38px;top:234px;width:240px;font-size:13.5px;line-height:14.3px;color:var(--ink)}
  .expertise{position:absolute;left:38px;top:336px;width:250px;font-size:11px;line-height:16px;color:var(--ink)}
  .expertise h4{font-weight:700;font-size:11px}
  .expertise li{list-style:none;padding-left:9px;text-indent:-9px}
  .expertise li::before{content:"• "}

  .headshot{position:absolute;left:292px;width:77px;height:79px;border:1px solid #fff;background:linear-gradient(180deg,#8ea4bd,#3d4c5f)}
  .member{position:absolute;left:388px;width:180px;font-size:11px;line-height:13px;color:var(--ink)}
  .member h3{font-size:17px;font-weight:400;color:var(--navy);line-height:18px}
  .member .creds{font-size:12.5px;line-height:16px;color:#111}

  .footer{position:absolute;left:36px;top:770px;color:#fff;font-size:12px;line-height:19px;text-transform:uppercase}

  .tagline{position:absolute;left:0;width:600px;top:130px;text-align:center;font-family:"Ubuntu",sans-serif;font-size:23px;color:var(--steel);letter-spacing:.3px}
  .warehouse-photo{position:absolute;left:0;top:174px;width:600px;height:675px;background:linear-gradient(90deg,#c8431c 0%,#2c2a26 30%,#f3efe5 48%,#2c2a26 66%,#c8431c 100%)}
  .headline{position:absolute;right:65px;top:548px;text-align:right;font-family:"Ubuntu",sans-serif;color:#fff;font-size:25.5px;line-height:28.5px;text-transform:uppercase}
  .pitch{position:absolute;right:65px;top:662px;width:420px;text-align:right;font-family:"Ubuntu",sans-serif;color:#fff;font-size:20.5px;line-height:28.5px}
  .pitch strong{font-weight:700}
</style>
</head>
<body>
<main class="spread">
  <svg class="spread-bg" width="1200" height="849" viewBox="0 0 1200 849" aria-hidden="true">
    <defs>
      <linearGradient id="leftBody" x1="0" y1="0" x2="0" y2="1">
        <stop offset="0" stop-color="#dfe6f3"/><stop offset="1" stop-color="#b7c8e6"/>
      </linearGradient>
      <linearGradient id="rightBlue" x1="1" y1="0" x2="0" y2="1">
        <stop offset="0" stop-color="#14b0e6"/><stop offset=".5" stop-color="#1f64b7"/><stop offset="1" stop-color="#173f86"/>
      </linearGradient>
      <linearGradient id="leftWave" x1="0" y1="0" x2="1" y2="0">
        <stop offset="0" stop-color="#1f4e97"/><stop offset="1" stop-color="#2a60b0"/>
      </linearGradient>
    </defs>
    <rect x="0" y="174" width="600" height="675" fill="url(#leftBody)"/>
    <path d="M0 380 C160 250 420 210 600 240 L600 174 L0 174 Z" fill="#e6ebf5" opacity=".7"/>
    <path d="M0 430 C200 330 420 320 600 360" stroke="#ffffff" stroke-opacity=".35" stroke-width="40" fill="none"/>
    <path d="M0 690 C90 670 180 705 260 735 C340 765 420 770 520 735 C560 718 590 700 600 690 L600 849 L0 849 Z" fill="url(#leftWave)"/>
    <path d="M0 750 C90 700 170 690 260 720 C360 755 460 760 560 715" stroke="#fff" stroke-width="3" fill="none"/>
    <path d="M0 690 C80 680 170 700 260 735" stroke="#fff" stroke-width="2" fill="none"/>
  </svg>

  <section class="page page-left">
    <div class="brand brand-small"><span class="brand-mark"></span>Meridian Logistics Group</div>
    <div class="route-map" role="img" aria-label="Map of Australia showing the national logistics route network"></div>

    <h2 class="section-title">OUR TEAM (WHO?)</h2>
    <p class="intro">With over 30 years or experience in warehouse, logistics and transportation and over 30 years of history in mergers, acquisitions and business sales, the Meridian team is uniquely qualified to deliver outcomes to its members.</p>

    <div class="expertise">
      <h4>Logistics industry expertise:</h4>
      <ul><li>Directors have &gt;30 years’ experience in warehouse, logistics and transportation</li></ul>
      <h4>Credibility from track record:</h4>
      <ul><li>30 year history in M&amp;A and business sales</li><li>National footprint</li><li>Operates under an AFSL</li></ul>
      <h4>M&amp;A and advisory expertise:</h4>
      <ul><li>&gt; $10B in combined transaction experience</li><li>Tier-1 level M&amp;A and advisory experience</li><li>Highly disciplined approach to business sales</li></ul>
      <h4>Breadth of expertise:</h4>
      <ul><li>Preparation and optimisation for sale</li><li>Business sales</li><li>Business acquisition and roll-ups</li><li>Logistics tender management</li><li>Logistics contract management</li><li>Professional business development</li><li>Business/profit improvement</li></ul>
    </div>

    <div class="headshot" style="top:207px" role="img" aria-label="Portrait of Daniel Hart"></div>
    <div class="member" style="top:199px">
      <h3>Daniel Hart</h3>
      <p class="creds">Bcomm • FAICD • CPA • FCILT</p>
      <p>•30 years’ warehouse, logistics, transportation experience in expansion, mergers, acquisitions and divestment</p>
      <p>• Established a national warehousing company</p>
      <p>• Managed sale and acquisition of warehouse business</p>
    </div>

    <div class="headshot" style="top:365px" role="img" aria-label="Portrait of Martin Selby"></div>
    <div class="member" style="top:358px">
      <h3>Martin Selby</h3>
      <p class="creds">B Eng • MAppFin • GAICD • FFinsia • CPEng • RPEQ</p>
      <p>• &gt;25 years’ international consulting, advisory experience</p>
      <p>• Mergers, acquisitions and divestment experience</p>
      <p>• Large bid management credentials leadings bids &gt; $500M</p>
      <p>• Responsible manager for Australian Financial Services License</p>
    </div>

    <div class="headshot" style="top:554px" role="img" aria-label="Portrait of Victor Pearce"></div>
    <div class="member" style="top:548px">
      <h3>Victor Pearce</h3>
      <p class="creds">CA • FCA • CEP</p>
      <p>• Ex-CFO of ultra-high growth businesses</p>
      <p>• Highly experienced in business roll-up strategies</p>
      <p>• Completed over 25 acquisitions and implementations</p>
      <p>• Executed divestment and merger programmes</p>
    </div>

    <div class="footer">
      <p>For further information</p>
      <p>Contact Daniel Hart: T: 07 3000 1200 &nbsp;M: &nbsp;&nbsp;0400 111 222 &nbsp;E: &nbsp;daniel.hart@meridianlg.com.au</p>
    </div>
  </section>

  <section class="page page-right">
    <div class="brand brand-large"><span class="brand-mark"></span>Meridian<br>Logistics Group</div>
    <p class="tagline">SCALE : SYNERGY : VALUE</p>
    <div class="warehouse-photo" role="img" aria-label="Photograph of a long warehouse aisle lined with orange and green pallet racking"></div>
    <svg style="position:absolute;left:0;top:0" width="600" height="849" viewBox="0 0 600 849" aria-hidden="true">
      <path d="M-10 849 L-10 470 C120 440 300 420 600 395 L600 849 Z" fill="url(#rightBlue)" opacity="0"/>
      <path d="M-12 849 C60 640 220 460 600 395 L600 849 Z" fill="url(#rightBlue)"/>
      <path d="M0 470 C140 420 360 400 600 395" stroke="#fff" stroke-opacity=".8" stroke-width="2" fill="none"/>
      <path d="M-12 849 C60 640 220 460 600 395" stroke="#fff" stroke-width="3" fill="none"/>
    </svg>
    <h1 class="headline">A new solution for<br>Australian warehouse<br>business owners</h1>
    <p class="pitch">Offering national <strong>scale</strong> to increase revenues, achieving <strong>synergies</strong> to reduce costs, and enhancing the <strong>value</strong> in your business.</p>
  </section>
</main>
</body>
</html>
```